Vindmark Health & Wellness needs a fresh and interesting website

I need a rebrand and redevelopment of my website, www.dellaquorne.example
Our mission is provide bespoke , lifestyle medicine , everyone has their own path to health. and we are creating a personalized experience for people to life their life to the fullest
Vindmark - means sea lands
I need an landing page and about page and potentially a few project launch pages , I have been using Wordpress for my basic information and then I use Plovix for the launch pages of my programs since I can edit those easily.

Target Market(s)

Corporate and individual's who are interested in a different perspective on health and wellness , and living with a chronic illness

Industry/Entity Type

Health, lifestyle , wellness coaching and medicine

Coding

Number of Pages Required

Font styles to use
Other font styles liked:
• look into the logo

Requirements
Must have
• the logo I uploaded
Nice to have
• I want a fresh perspective on health, I have bamboo, hibiscus vibes in my logo , but also like more of a water vibe/ I want something earthy but not too boho it needs to be clean
Should not have
• every other holistic health vibe,

```html
<!DOCTYPE html>
<html lang="en">
<head>
<meta charset="utf-8">
<title>Vindmark Health &amp; Wellness</title>
<link href="https://fonts.googleapis.com/css2?family=Noto+Serif:wght@400;500&family=Poppins:wght@300;400;500;600&display=swap" rel="stylesheet">
<style>
:root{
  --teal:#0b5a6e;
  --teal-dark:#0a4a5c;
  --blue:#1ba3d3;
  --green:#5aa53b;
  --green-light:#7cbf4a;
  --ink:#333;
  --muted:#666;
  --grey-band:#f1f1f3;
  --white:#fff;
}
*{box-sizing:border-box;margin:0;padding:0}
html,body{width:1200px;height:5195px;overflow:hidden}
body{position:relative;font-family:"Poppins",sans-serif;color:var(--ink);background:var(--white)}
.abs{position:absolute}
.serif{font-family:"Noto Serif",serif;font-weight:400}
.btn{position:absolute;display:flex;align-items:center;justify-content:center;border-radius:20px;font-size:11px;font-weight:500;color:var(--white);text-transform:uppercase;letter-spacing:.3px}
.btn-teal{background:linear-gradient(90deg,var(--teal-dark),var(--blue))}
.dots{position:absolute;display:flex;gap:5px}
.dots i{width:6px;height:6px;border-radius:50%;background:var(--blue);display:block}

/* header */
.site-header{position:absolute;left:0;top:0;width:1200px;height:130px}
.brand{position:absolute;left:78px;top:46px;display:flex;align-items:center;gap:12px}
.brand-mark{width:34px;height:34px;border-radius:50%;background:var(--blue)}
.brand-name{font-family:"Noto Serif",serif;font-size:28px;color:var(--teal);line-height:1}
.nav{position:absolute;top:62px;left:515px;display:flex;gap:36px;font-size:12px;color:#444;text-transform:uppercase}
.nav .active{color:var(--teal);border-bottom:2px solid var(--blue);padding-bottom:6px}
.nav-cta{left:1003px;top:53px;width:122px;height:36px;background:var(--teal);font-size:12px}

/* hero */
.hero{position:absolute;left:0;top:130px;width:1200px;height:708px;background:linear-gradient(100deg,#31431f 0%,#5d7a3a 35%,#8a9b6a 60%,#6f8a4a 100%)}
.hero-title{position:absolute;left:77px;top:110px;font-size:64px;line-height:94px;letter-spacing:1px;background:linear-gradient(90deg,#9ccc3c,#38b6d9);-webkit-background-clip:text;background-clip:text;color:transparent}
.hero-sub{position:absolute;left:78px;top:316px;width:430px;font-size:22px;line-height:34px;color:var(--white);font-weight:300}
.hero-cta{left:75px;top:458px;width:124px;height:40px;border:2px solid var(--white);background:var(--teal);font-size:11px}

/* about */
.about-photo-ring{left:66px;top:1018px;width:506px;height:506px;border-radius:50%;background:#e8e8e8}
.about-photo{left:88px;top:1040px;width:462px;height:462px;border-radius:50%;background:linear-gradient(160deg,#5f7c44,#a4737a 55%,#5a6e86)}
.about-dot{left:122px;top:993px;width:64px;height:64px;border-radius:50%;background:var(--blue)}
.about-ring{left:414px;top:1447px;width:110px;height:110px;border-radius:50%;border:7px solid var(--green-light)}
.about-title{left:633px;top:1085px;font-size:48px;color:var(--teal)}
.about-name{left:634px;top:1146px;font-size:22px;color:var(--green)}
.about-text{left:634px;top:1205px;width:466px;font-size:12.5px;line-height:26px;color:#555}
.about-text em{font-style:normal;font-size:20px;color:var(--blue)}
.about-cta{left:633px;top:1372px;width:120px;height:38px;background:var(--teal)}

/* why */
.why{position:absolute;left:0;top:1645px;width:1200px;height:338px;background:var(--grey-band)}
.why-title{left:74px;top:65px;font-size:52px;color:var(--teal)}
.why-sub{left:78px;top:128px;font-size:20px;color:var(--green);letter-spacing:1px}
.why-line{left:78px;top:143px;width:320px;height:1px;background:var(--blue);margin-top:15px}
.why-items{position:absolute;left:78px;top:205px;display:flex;gap:56px}
.why-item{display:flex;align-items:center;gap:10px;font-size:13px;line-height:16px;color:var(--teal)}
.why-icon{width:64px;height:64px;border-radius:50%;background:linear-gradient(135deg,var(--teal),var(--blue));border:4px solid #d8ecf3}
.plant{left:780px;top:1610px;width:400px;height:392px;border-radius:50%;background:radial-gradient(circle,#3f8a52,#2a6a3c 60%,#1f4d2c)}

/* section heads */
.section-head{position:absolute;left:0;width:1200px;text-align:center}
.section-head h2{font-family:"Noto Serif",serif;font-weight:400;font-size:52px;color:var(--teal);line-height:1}
.section-head p{display:inline-flex;align-items:center;gap:16px;margin-top:8px;font-size:21px;color:var(--green);letter-spacing:.5px}
.section-head p::before,.section-head p::after{content:"";width:80px;height:1px;background:var(--blue)}

/* services */
.service-card{position:absolute;top:2340px;width:236px;height:292px;border:2px solid #dcdcdc;border-radius:6px;background:var(--white);overflow:hidden}
.service-photo{height:210px}
.service-icon{position:absolute;left:92px;top:185px;width:50px;height:50px;border-radius:50%;background:linear-gradient(135deg,var(--teal),var(--blue));border:3px solid var(--white)}
.service-name{position:absolute;left:0;top:244px;width:100%;text-align:center;font-size:22px;color:var(--teal)}
.service-card.featured{background:linear-gradient(180deg,#2d4c4d,#3d5a58);border-color:var(--teal)}
.featured .service-icon{top:16px}
.featured h3{position:absolute;top:74px;width:100%;text-align:center;font-weight:400;font-size:22px;color:var(--white)}
.featured p{position:absolute;top:120px;left:20px;right:20px;text-align:center;font-size:12.5px;line-height:22px;color:var(--white)}
.featured .btn{left:75px;top:228px;width:86px;height:22px;background:var(--blue);font-size:8px}

/* join */
.join-photo{left:0;top:2840px;width:856px;height:550px;background:linear-gradient(90deg,#c4a57e,#e4c89e 45%,#8b7458 75%,#d7b888)}
.join-circle{left:610px;top:2865px;width:492px;height:492px;border-radius:50%;background:linear-gradient(135deg,#0b4f66,var(--teal) 40%,var(--blue));border:10px solid #f3f3f3}
.join-title{position:absolute;left:0;top:180px;width:100%;text-align:center;font-size:30px;line-height:40px;color:var(--white)}
.join-text{position:absolute;left:55px;width:362px;top:268px;text-align:center;font-size:13px;line-height:27px;color:var(--white)}
.join-cta{left:166px;top:385px;width:148px;height:42px;background:var(--green);font-size:12px}

/* testimonials */
.review{position:absolute;top:3715px;width:330px;height:262px;background:var(--white);box-shadow:0 0 14px rgba(0,0,0,.12);border-bottom:4px solid var(--teal)}
.review-avatar{position:absolute;left:22px;top:22px;width:64px;height:64px;border-radius:50%;background:#c9c4bc;border:3px solid #eee}
.review-name{position:absolute;left:106px;top:36px;font-size:15px;color:var(--teal);font-weight:500}
.review-role{position:absolute;left:106px;top:56px;font-size:11px;color:#555}
.review-stars{position:absolute;left:106px;top:68px;font-size:11px;color:#f4b400;letter-spacing:1px}
.review-text{position:absolute;left:26px;top:110px;width:290px;font-size:13px;line-height:23px;color:#555}
.review-quote{position:absolute;right:24px;top:194px;display:flex;gap:6px}
.review-quote i{display:block;width:16px;height:20px;background:#ddd}
.pager{position:absolute;left:566px;top:4021px;display:flex;gap:12px}
.pager i{display:block;width:7px;height:7px;border-radius:50%;background:#c8dde6}
.pager i.on{background:var(--blue)}

/* contact */
.contact-band{left:0;top:4560px;width:1200px;height:272px;background:linear-gradient(90deg,#0c5a66,#2f8a55 60%,var(--green))}
.contact-card{left:75px;top:4170px;width:1052px;height:650px;border-radius:30px;background:var(--white);border:4px solid #cfe6ee;overflow:hidden}
.contact-photo{position:absolute;left:0;top:0;width:540px;height:100%;background:linear-gradient(160deg,#4f7e3d,#a5443e 45%,#c6998f 70%,#6b7f5b)}
.contact-title{position:absolute;left:615px;top:70px;font-size:52px;color:var(--teal)}
.contact-rule{position:absolute;left:740px;top:148px;width:80px;height:2px;background:var(--blue)}
.contact-text{position:absolute;left:605px;top:180px;width:380px;text-align:center;font-size:12.5px;line-height:24px;color:#555}
.field{position:absolute;left:605px;width:380px;height:48px;border:1px solid #e4e4e4;box-shadow:0 2px 6px rgba(0,0,0,.06);padding:15px 20px;font-size:12px;color:#555}
.contact-submit{left:746px;top:4743px;width:98px;height:30px;background:var(--teal);font-size:11px}

/* footer */
.site-footer{position:absolute;left:0;top:4832px;width:1200px;height:363px;background:linear-gradient(90deg,#0b4a5d,#0e5a62 55%,#2a7a4c)}
.foot-brand{position:absolute;left:94px;top:150px;display:flex;align-items:center;gap:12px}
.foot-brand .brand-mark{background:var(--white);width:30px;height:30px}
.foot-brand .brand-name{color:var(--white);font-size:40px}
.foot-social{position:absolute;left:173px;top:248px;display:flex;gap:10px}
.foot-social i{display:block;width:32px;height:32px;border:2px solid #cfd9da;border-radius:4px}
.foot-col{position:absolute;top:55px;color:var(--white)}
.foot-col::before{content:"";position:absolute;left:-22px;top:10px;width:1px;height:230px;background:rgba(255,255,255,.35)}
.foot-col::after{content:"";position:absolute;left:-26px;top:4px;width:9px;height:9px;border-radius:50%;background:var(--green-light)}
.foot-col h4{font-weight:400;font-size:16px;letter-spacing:.5px;margin-bottom:30px}
.foot-col li{list-style:none;font-size:12px;margin-bottom:12px}
.contact-line{display:flex;gap:16px;margin-bottom:20px;font-size:12px;line-height:14px}
.contact-line span.ic{width:26px;height:26px;border:2px solid var(--white);border-radius:4px;flex:none;display:flex;align-items:center;justify-content:center}
.news-input{margin-top:16px;width:210px;height:34px;border:1px solid rgba(255,255,255,.7);border-radius:20px;font-size:10px;padding:10px 18px;position:relative}
.news-input i{position:absolute;right:4px;top:4px;width:24px;height:24px;border:1px solid var(--green-light);border-radius:50%}
.copyright{position:absolute;left:0;top:323px;width:1200px;height:40px;background:#0a3e50;text-align:center;line-height:40px;font-size:11px;color:var(--white)}
</style>
</head>
<body>

<header class="site-header">
  <div class="brand"><span class="brand-mark"></span><span class="brand-name">Vindmark</span></div>
  <nav class="nav">
    <span class="active">Home</span><span>About Us</span><span>Services</span><span>Fall Mini Retreat</span><span>Blog</span>
  </nav>
  <span class="btn nav-cta">Contact Us</span>
</header>

<section class="hero" role="img" aria-label="Woman meditating cross-legged on a wooden boardwalk among green grass">
  <h1 class="hero-title serif">JOURNEY OF<br>HOLISTIC HEALING</h1>
  <p class="hero-sub">where art, science, and compassion converge to create a healthier, happier community.</p>
  <span class="btn hero-cta">Contact Us</span>
</section>

<div class="abs about-photo-ring"></div>
<div class="abs about-photo" role="img" aria-label="Portrait of the practitioner in a red hat and pink scarf, seated outdoors"></div>
<div class="abs about-dot"></div>
<div class="abs about-ring"></div>
<div class="dots" style="left:636px;top:1072px"><i></i><i></i><i></i></div>
<h2 class="abs about-title serif">ABOUT ME</h2>
<p class="abs about-name">Dr Della P Quorne DACM, L.Ac.</p>
<p class="abs about-text">At a young age, I discovered the transformative power of Eastern Medicine when it helped me overcome lung concerns, propelling me toward my dreams as a young athlete. Years later, I faced a pivotal choice: How could I best serve and heal my community? The answer was crystal clear—<em>Eastern Medicine.</em></p>
<span class="btn about-cta">Know More</span>

<section class="why">
  <div class="dots" style="left:78px;top:45px"><i></i><i></i><i></i></div>
  <h2 class="abs why-title serif">WHY CHOOSE</h2>
  <p class="abs why-sub">VINDMARK</p>
  <div class="abs why-line"></div>
  <div class="why-items">
    <div class="why-item"><span class="why-icon"></span>Highest level<br>of expertise</div>
    <div class="why-item"><span class="why-icon"></span>National certification<br>in the USA</div>
    <div class="why-item"><span class="why-icon"></span>24/7 Support</div>
  </div>
</section>
<div class="abs plant" role="img" aria-label="Green succulent plant in a pot seen from above"></div>

<div class="dots" style="left:584px;top:2120px"><i></i><i></i><i></i></div>
<div class="section-head" style="top:2140px"><h2>OUR SERVICES</h2><p>WHAT WE DO</p></div>

<article class="service-card" style="left:75px">
  <div class="service-photo" role="img" aria-label="Group yoga class with raised arms" style="background:linear-gradient(135deg,#8a8f95,#c9c3bb)"></div>
  <span class="service-icon"></span><h3 class="service-name" style="font-weight:400">Yoga</h3>
</article>
<article class="service-card" style="left:338px">
  <div class="service-photo" role="img" aria-label="Back massage treatment" style="background:linear-gradient(135deg,#a9765e,#e7c3a9)"></div>
  <span class="service-icon"></span><h3 class="service-name" style="font-weight:400">Massage</h3>
</article>
<article class="service-card featured" style="left:600px">
  <span class="service-icon"></span>
  <h3>Healthy food</h3>
  <p>Lorem ipsum dolor sit amet, consectetur adipiscing elit, sed do eiusmod tempor inc ididunt ut labore et dolore</p>
  <span class="btn">Read More</span>
</article>
<article class="service-card" style="left:863px">
  <div class="service-photo" role="img" aria-label="Relaxing spa facial treatment" style="background:linear-gradient(135deg,#6c4a38,#c79c84)"></div>
  <span class="service-icon"></span><h3 class="service-name" style="font-weight:400">Retreats</h3>
</article>

<div class="abs join-photo" role="img" aria-label="Woman stacking balanced stones at sunset"></div>
<div class="abs join-circle">
  <h2 class="join-title serif">JOIN ME ON THIS JOURNEY<br>OF HOLISTIC HEALING</h2>
  <p class="join-text">where art, science, and compassion converge to create a healthier, happier community. Let's explore the profound possibilities of Eastern Medicine together!</p>
  <span class="btn join-cta">Contact Us</span>
</div>

<div class="dots" style="left:584px;top:3515px"><i></i><i></i><i></i></div>
<div class="section-head" style="top:3535px"><h2>TESTIMONIALS</h2><p>CLIENT REVIEWS</p></div>

<article class="review" style="left:78px">
  <span class="review-avatar"></span><span class="review-name">Jonathan Smith</span><span class="review-role">Client</span><span class="review-stars">★★★★★</span>
  <p class="review-text">Lorem ipsum dolor sit amet, consectetur adipiscing elit, sed do eiusmod tempor incididunt ut labore et dolore magna aliqua. Quis ipsum suspendisse ultrices gravida. Risus commodo viverra</p>
  <span class="review-quote"><i></i><i></i></span>
</article>
<article class="review" style="left:435px">
  <span class="review-avatar"></span><span class="review-name">Jonathan Smith</span><span class="review-role">Client</span><span class="review-stars">★★★★★</span>
  <p class="review-text">Lorem ipsum dolor sit amet, consectetur adipiscing elit, sed do eiusmod tempor incididunt ut labore et dolore magna aliqua. Quis ipsum suspendisse ultrices gravida. Risus commodo viverra</p>
  <span class="review-quote"><i></i><i></i></span>
</article>
<article class="review" style="left:792px">
  <span class="review-avatar"></span><span class="review-name">Jonathan Smith</span><span class="review-role">Client</span><span class="review-stars">★★★★★</span>
  <p class="review-text">Lorem ipsum dolor sit amet, consectetur adipiscing elit, sed do eiusmod tempor incididunt ut labore et dolore magna aliqua. Quis ipsum suspendisse ultrices gravida. Risus commodo viverra</p>
  <span class="review-quote"><i></i><i></i></span>
</article>
<div class="pager"><i class="on"></i><i></i><i></i><i></i></div>

<div class="abs contact-band"></div>
<section class="abs contact-card">
  <div class="contact-photo" role="img" aria-label="Smiling practitioner in a red hat and knitted scarf outdoors"></div>
  <h2 class="contact-title serif">CONTACT US</h2>
  <span class="contact-rule"></span>
  <p class="contact-text">Lorem ipsum dolor sit amet, consectetur adipiscing elit, sed do eiusmod tempor incididunt ut labore</p>
  <div class="field" style="top:253px">Your Name</div>
  <div class="field" style="top:315px">Phone Number</div>
  <div class="field" style="top:377px">Email Address</div>
  <div class="field" style="top:439px;height:88px">Message</div>
</section>
<span class="btn contact-submit">Submit</span>

<footer class="site-footer">
  <div class="foot-brand"><span class="brand-mark"></span><span class="brand-name">Vindmark</span></div>
  <div class="foot-social"><i></i><i></i></div>
  <div class="foot-col" style="left:422px">
    <h4>QUICK LINKS</h4>
    <ul><li>About Us</li><li>Services</li><li>Fall Mini Retreat</li><li>Blog</li><li>Contact Us</li></ul>
  </div>
  <div class="foot-col" style="left:642px">
    <h4>CONTACT US</h4>
    <div class="contact-line"><span class="ic"><svg width="12" height="12" viewBox="0 0 24 24" fill="none" stroke="#fff" stroke-width="2.5"><path d="M5 3h4l2 5-3 2a12 12 0 0 0 6 6l2-3 5 2v4a2 2 0 0 1-2 2A18 18 0 0 1 3 5a2 2 0 0 1 2-2z"/></svg></span><span>CALL US<br>8012 555 0147</span></div>
    <div class="contact-line"><span class="ic"><svg width="12" height="10" viewBox="0 0 24 18" fill="none" stroke="#fff" stroke-width="2.5"><rect x="1" y="1" width="22" height="16"/><path d="M1 1l11 9 11-9"/></svg></span><span>EMAIL US<br>info@vindmark.example</span></div>
    <div class="contact-line"><span class="ic"><svg width="10" height="13" viewBox="0 0 20 26" fill="none" stroke="#fff" stroke-width="2.5"><path d="M10 25s8-9 8-15a8 8 0 0 0-16 0c0 6 8 15 8 15z"/><circle cx="10" cy="10" r="3"/></svg></span><span>Address line Dummy Here<br>Address line Here</span></div>
  </div>
  <div class="foot-col" style="left:940px">
    <h4>NEWSLETTER SIGN UP</h4>
    <p style="font-size:12px;line-height:15px;width:220px">Subscribe our newsletter to get the latest news.</p>
    <div class="news-input">Enter Email Address<i></i></div>
  </div>
  <div class="copyright">Copyright © 2024 All Rights Reserved By Company name</div>
</footer>

</body>
</html>
```